Comparison Website Design for Glue Website

Note: We don't have a logo, it's not needed. Just put placeholder.

We would like a website comparing A to B, simple elegant design, simplistic styling. Website is for helping people find the best glue to glue 2 things together. For example, Metal to wood, Metal to rubber, glass to fabric and so on. Select 2 options and be shown the best glue/adhesive for the job.

Purpose of the website:
Allowing someone to pick 2 materials they want to glue together, and showing them the best product for it. We want someone to select 2 materials like "Metal and Rubber". It'll then show the best glues/adhesives from best #1 to #5-10 other ones. The design is simple and doesn't need much detail.

Design rules:
Please design using bootstrap 4 with a modified 1440px width.

We're looking for 4 main pages:
Home Page, Compare Page, Category Page, Product Page.

Target Market(s)

Everyone

Industry/Entity Type

Adhesive

Number of Pages Required

3 page

Font styles to use
Sans Serif

Colors
876aae
b7a5cd
6b449b
e4daeb
fefeff

Requirements
Must have
• We like the following features of these designs:
https://pixelvane.example/shots/6401517-CoverLoom-Dashboard - Main menu with the drop down, this will change depending on the active page. If they are on a metal page they could be shown "glue metal to ___" options. We also like the simple table view in this design under "users" heading.

https://pixelvane.example/shots/6300662-Volt-Sketch-Quotation-Page - The entire colour palette is great! The simplicity of the design is great.

https://pixelvane.example/shots/8593973-Loans-Comparison-UI - The boxes at the top look great, if there was 2 of these with a compare icon between them and above that saying "glue metal to rubber" and it shows an icon/image or metal and glue... The table of products is also good, it has dot points and details which we like.

https://pixelvane.example/shots/4586351-Transfer-Money/attachments/4586351-Transfer-Money?mode=media - The right it shows which 2 products are selected (metal and rubber) for example, on the left it would say "best glue for metal and rubber". This is too detailed though, so it would need to be simplified nicely.

https://linquora.example/ - They do a good job of "comparing" 2 things and displaying integrations well. You can get lots of ideas from them linking A to B similar to what we want to show.

https://www.campaignflowreview.example/leadnest-vs-drivemint/ - This shows a good example of the hero section how it should look.

Features of each page to help you design:
Home Page-
Menu (shown in examples above)
Hero section (colour section) with a centre heading saying "what do you want to glue together" with 2 boxes below to select materials from.
List of most popular searches (metal to rubber, glass to wood, fabric to leather... repeat these to fill space).
List of popular products with basic details about each one (grid format, not list).
FAQs - You choose design for this
Content section (simple design, headings, paragraphs, dotpoints, images...)
Blog section - Simple 3 column grid with an image on top, heading, paragraph, button.

Compare Page-
Showing 2 materials in the colour hero section under or to the right of the heading and paragraph.
Best product (highlighted)
9 other products (list table)
3 column section saying glue (product a to ___) with other product that isn't product b + reverse of this.
Content section

Category page-
heading and breadcrumbs in hero section
Standard product list 1 column on the left with filters, 3 products shown on the right in grid format with basic details on each one.

Product page-
Image left, details on the right.
Keep the image smaller not 50% as we want it to not take up too much space vertically.
Under this put a table where this product ranks for gluing things together. for example #3 for gluing metal to rubber, #1 for glass to wood.
Content section.

Please note, keep this design flat, simple and pretty. We don't need it over-designed or detailed, we simply want a simple functionality website that clearly shows what we're looking for.

```html
<!DOCTYPE html>
<html lang="en">
<head>
<meta charset="utf-8">
<title>Glue Compare – Home</title>
<link href="https://fonts.googleapis.com/css2?family=Poppins:wght@400;500;600;700&display=swap" rel="stylesheet">
<style>
:root{
  --purple-dark:#6b449b;
  --purple:#876aae;
  --purple-soft:#b7a5cd;
  --lilac:#e4daeb;
  --lilac-bg:#f7f2fb;
  --tile-bg:#f6f3fa;
  --white:#fefeff;
  --ink:#222222;
  --muted:#555555;
  --line:#d9d9d9;
}
*{box-sizing:border-box;margin:0;padding:0}
html,body{width:1200px;height:2920px;overflow:hidden}
body{font-family:'Poppins',sans-serif;color:var(--ink);background:var(--white);position:relative}
.abs{position:absolute}

/* header */
.site-header{position:absolute;left:0;top:0;width:1200px;height:68px;background:#fff}
.logo{left:87px;top:20px;font-size:20px;font-weight:600;color:var(--ink)}
.main-nav{right:90px;top:0;height:68px;display:flex;align-items:center;gap:24px}
.main-nav a{font-size:14px;font-weight:500;color:var(--ink);text-decoration:none}
.main-nav a.active{color:var(--purple)}
.user{display:flex;align-items:center;gap:8px;margin-left:0}
.avatar{width:34px;height:34px;border-radius:50%;background:linear-gradient(135deg,#c9866a,#7b4a3a)}
.user small{display:block;font-size:10px;color:var(--purple);line-height:1;font-weight:500}
.user strong{display:block;font-size:15px;font-weight:500;line-height:1.1}

/* hero */
.hero{left:0;top:68px;width:1200px;height:508px;background:linear-gradient(120deg,#6b449b 0%,#7550a6 60%,#7f5db0 100%)}
.hero h1{left:0;top:112px;width:1200px;text-align:center;color:#fff;font-size:40px;line-height:43px;font-weight:700}
.upload-btn{left:544px;top:218px;width:112px;height:34px;background:#fff;border-radius:3px;font-size:17px;font-weight:600;text-align:center;line-height:34px;color:var(--ink)}
.material-box{top:266px;width:175px;height:131px;border:2px dashed #fff;border-radius:8px;color:#fff;text-align:center;box-shadow:0 12px 24px rgba(40,10,80,.18)}
.material-box svg{margin-top:20px}
.material-box span{display:block;font-size:18px;font-weight:600;margin-top:6px}
.vs{left:575px;top:309px;width:50px;height:50px;border:2px dashed #fff;border-radius:50%;color:#fff;font-size:18px;text-align:center;line-height:46px}

/* popular searches */
.section-title{width:1200px;left:0;text-align:center;font-size:34px;font-weight:600}
.search-tile{top:731px;width:133px;height:130px;background:var(--tile-bg);border-radius:8px;display:flex;align-items:center;justify-content:center}
.search-tile.active{background:#fff;border:2px solid var(--purple)}
.search-label{top:880px;width:160px;text-align:center;font-size:16px;font-weight:600}

/* popular products */
.products-band{left:0;top:994px;width:1200px;height:325px;background:var(--lilac-bg);overflow:hidden}
.products-band h2{left:89px;top:122px;font-size:35px;font-weight:600}
.show-all{left:89px;top:177px;width:141px;height:39px;background:var(--purple-dark);color:#fff;border-radius:4px;font-size:16px;font-weight:600;text-align:center;line-height:39px}
.product-card{width:411px;height:81px;background:#fff;border-left:5px solid var(--purple);border-radius:6px;padding:20px 0 0 24px;box-shadow:0 6px 16px rgba(107,68,155,.08)}
.product-card h3{font-size:18px;font-weight:600;line-height:20px}
.product-card p{font-size:14px;color:var(--muted);line-height:18px}

/* faq */
.faq-item{left:326px;width:547px;height:58px;border-bottom:1px solid var(--line);display:flex;align-items:center;justify-content:space-between;padding:0 14px}
.faq-item span{font-size:18px;font-weight:500}
.faq-plus{width:22px;height:22px;border-radius:50%;background:var(--purple);color:#fff;font-size:16px;line-height:22px;text-align:center;font-weight:600}

/* content */
.dots-bg{left:0;top:1775px;width:210px;height:244px;background:var(--lilac);opacity:.8}
.content-photo{left:88px;top:1810px;width:506px;height:345px;border-radius:10px;background:linear-gradient(140deg,#c7b5dc,#a98dc9)}
.content-text{left:635px;top:1868px;width:480px}
.content-text h2{font-size:36px;font-weight:600;margin-bottom:8px}
.content-text p{font-size:16px;line-height:25px;color:var(--muted);padding-left:3px}
.content-text ul{list-style:none;margin-top:12px;padding-left:3px}
.content-text li{font-size:16px;line-height:25px;color:var(--muted);padding-left:19px;position:relative}
.content-text li::before{content:"";position:absolute;left:4px;top:10px;width:6px;height:6px;border-radius:50%;background:var(--purple-soft)}

/* blog */
.blog-card{top:2312px;width:322px;height:372px;background:#fff;border-radius:10px;overflow:hidden;box-shadow:0 10px 30px rgba(0,0,0,.08)}
.blog-img{width:322px;height:206px}
.blog-body{padding:26px 34px 0}
.blog-body h3{font-size:22px;font-weight:600;line-height:26px}
.blog-body p{font-size:13px;line-height:18px;color:var(--muted);margin-top:8px}
.blog-body a{display:block;margin-top:6px;font-size:13px;font-weight:600;color:var(--purple);text-decoration:none}

/* footer */
.site-footer{left:0;top:2790px;width:1200px;height:130px;background:var(--purple-dark);color:#fff;text-align:center}
.footer-nav{display:flex;justify-content:center;gap:24px;margin-top:50px}
.footer-nav a{color:#fff;text-decoration:none;font-size:15px;font-weight:500}
.copyright{font-size:13px;margin-top:4px}
.to-top{left:1132px;top:64px;width:30px;height:30px;border-radius:50%;background:var(--purple);}
</style>
</head>
<body>

<header class="site-header">
  <div class="logo abs">Logo Here</div>
  <nav class="main-nav abs">
    <a href="#" class="active">Home</a>
    <a href="#">Compare</a>
    <a href="#">Category</a>
    <a href="#">Product</a>
    <a href="#">Contact Us</a>
    <div class="user">
      <div class="avatar" role="img" aria-label="User profile photo"></div>
      <div><small>Welcome</small><strong>Dale Harlow</strong></div>
    </div>
  </nav>
</header>

<section class="hero abs">
  <h1 class="abs">What do you<br>Want to glue together</h1>
  <div class="upload-btn abs">Upload</div>
  <div class="material-box abs" style="left:338px">
    <svg width="36" height="66" viewBox="0 0 36 66" fill="#fff"><path d="M16 0h4l2 10h-8z"/><rect x="11" y="10" width="14" height="8" rx="1"/><rect x="3" y="18" width="30" height="46" rx="5"/><rect x="7" y="38" width="22" height="14" fill="#6e47a0"/></svg>
    <span>Glue metal</span>
  </div>
  <div class="vs abs">VS</div>
  <div class="material-box abs" style="left:687px">
    <svg width="62" height="60" viewBox="0 0 62 60" fill="none" stroke="#fff" stroke-width="4"><path d="M40 4l18 18-32 32H12L4 46z" fill="#fff"/><path d="M24 20l18 18" stroke="#6e47a0"/><path d="M8 50l10 6" /></svg>
    <span>Rubber</span>
  </div>
</section>

<h2 class="section-title abs" style="top:658px">List of most popular searches</h2>

<div class="search-tile abs" style="left:243px">
  <svg width="70" height="40" viewBox="0 0 70 40" fill="#8466b0"><path d="M40 2l28 10-36 26L2 28z"/><path d="M22 18l16 10" stroke="#fff" stroke-width="3"/></svg>
</div>
<div class="search-tile abs" style="left:388px">
  <svg width="44" height="62" viewBox="0 0 44 62" fill="none" stroke="#8466b0" stroke-width="3"><path d="M3 3h38l-5 56H8z"/><path d="M6 34h32l-3 25H9z" fill="#8466b0"/></svg>
</div>
<div class="search-tile abs active" style="left:534px">
  <svg width="62" height="62" viewBox="0 0 62 62" fill="none" stroke="#8466b0" stroke-width="3"><rect x="6" y="6" width="50" height="50" rx="8"/><path d="M6 18h50M6 31h50M6 44h50M18 6v50M31 6v50M44 6v50"/></svg>
</div>
<div class="search-tile abs" style="left:679px">
  <svg width="54" height="62" viewBox="0 0 54 62" fill="none" stroke="#8466b0" stroke-width="3"><ellipse cx="14" cy="46" rx="11" ry="12"/><path d="M3 46V14a11 12 0 0 1 22 0v32M25 14h20l6 14v32H14"/></svg>
</div>
<div class="search-tile abs" style="left:824px">
  <svg width="66" height="56" viewBox="0 0 66 56" fill="#8466b0"><path d="M2 16L28 2l36 18-26 14z"/><path d="M2 26l36 18 26-14v6L38 50 2 32z"/><path d="M2 38l36 18 26-14v-4L38 52 2 34z"/></svg>
</div>
<div class="search-label abs" style="left:227px">Metal to rubber</div>
<div class="search-label abs" style="left:372px">Glass to wood</div>
<div class="search-label abs" style="left:520px">Fabric to leather</div>
<div class="search-label abs" style="left:669px">Glass to wood</div>
<div class="search-label abs" style="left:811px">Fabric to leather</div>

<section class="products-band abs">
  <h2 class="abs">List of popular products</h2>
  <div class="show-all abs">SHOW ALL</div>
  <div class="product-card abs" style="left:578px;top:55px"><h3>Metal to rubber</h3><p>Lorem Ipsum is simply dummy text of the printing.</p></div>
  <div class="product-card abs" style="left:645px;top:151px"><h3>Glass to wood</h3><p>Lorem Ipsum is simply dummy text of the printing.</p></div>
  <div class="product-card abs" style="left:699px;top:246px"><h3>Fabric to leather</h3><p>Lorem Ipsum is simply dummy text of the printing.</p></div>
</section>

<h2 class="section-title abs" style="top:1411px">FAQs</h2>
<div class="faq-item abs" style="top:1468px"><span>Lorem Ipsum is simply dummy text ?</span><div class="faq-plus">+</div></div>
<div class="faq-item abs" style="top:1526px"><span>Printing and typesetting industry ?</span><div class="faq-plus">+</div></div>
<div class="faq-item abs" style="top:1584px"><span>The industry's standard dummy text ?</span><div class="faq-plus">+</div></div>
<div class="faq-item abs" style="top:1642px"><span>Ever since the 1500s ?</span><div class="faq-plus">+</div></div>

<div class="dots-bg abs" role="img" aria-label="Decorative dotted pattern"></div>
<div class="content-photo abs" role="img" aria-label="Photo of a smiling woman in a lilac t-shirt shrugging against a lilac wall"></div>
<div class="content-text abs">
  <h2>Comparing A to B</h2>
  <p>Lorem Ipsum is simply dummy text of the printing and typeset-ting industry. Lorem Ipsum has been the industry's standard dummy text ever since the 1500s, when an unknown printer took a galley of type and scrambled it to make .</p>
  <ul>
    <li>Lorem Ipsum is simply dummy text.</li>
    <li>Of the printing and typesetting.</li>
    <li>Industry Lorem Ipsum has been the industry's standard.</li>
  </ul>
</div>

<h2 class="section-title abs" style="top:2242px">Latest Blog</h2>
<article class="blog-card abs" style="left:97px">
  <div class="blog-img" role="img" aria-label="Close-up of wavy chrome metal surface" style="background:linear-gradient(135deg,#e8e8e8,#6f6f6f 50%,#d9d9d9)"></div>
  <div class="blog-body"><h3>Blog Heading Here</h3><p>Lorem Ipsum is simply dummy text of the printing and typesetting industry. Lorem Ipsum has been the industry's .</p><a href="#">READ MORE</a></div>
</article>
<article class="blog-card abs" style="left:439px">
  <div class="blog-img" role="img" aria-label="Close-up of woven glass fibre fabric" style="background:linear-gradient(135deg,#cfcfcf,#a9a9a9 55%,#c8d4bf)"></div>
  <div class="blog-body"><h3>Blog Heading Here</h3><p>Lorem Ipsum is simply dummy text of the printing and typesetting industry. Lorem Ipsum has been the industry's .</p><a href="#">READ MORE</a></div>
</article>
<article class="blog-card abs" style="left:780px">
  <div class="blog-img" role="img" aria-label="Drill driving screws into wooden deck boards" style="background:linear-gradient(180deg,#c9a57b,#d8b68c 60%,#2c2f3a)"></div>
  <div class="blog-body"><h3>Blog Heading Here</h3><p>Lorem Ipsum is simply dummy text of the printing and typesetting industry. Lorem Ipsum has been the industry's .</p><a href="#">READ MORE</a></div>
</article>

<footer class="site-footer abs">
  <nav class="footer-nav">
    <a href="#">Home</a><a href="#">Compare</a><a href="#">Category</a><a href="#">Product</a><a href="#">Contact Us</a>
  </nav>
  <div class="copyright">Copyright 2020 | All Rights Reserved</div>
  <div class="to-top abs"><svg width="30" height="30" viewBox="0 0 30 30" fill="none" stroke="#fff" stroke-width="1.6"><path d="M12 17l3-3 3 3"/></svg></div>
</footer>

</body>
</html>
```